Policies Manual Design & Formatting

My company currently has complete bylaws and policies organized as needed. We would like them formatted in Word to look professional and easily editable.

We have all text and titles completed and a brand book to guide text and colors. We would also like the designer to gather design inspiration from our website brenwickguild.org.

Text word file upload coming on 10/18

Industry/Entity Type

Business Consultant

Font styles to use
Serif
Sans Serif
Other font styles liked:
• Montserrat and Domine

Colors

Designer to choose colors to be used in the design.

Requirements
Must have
• Montserrat and domine fonts
• Colors from brand book file
• layout and print formatting
• dynamic Table of Contents
• Incorporate logo and company information
• Include automatic page numbers
• Modify or add headers/footer
• Profeasional cover page

```html
<!DOCTYPE html>
<html lang="en">
<head>
<meta charset="utf-8">
<title>Brenwick Chamber Bylaws</title>
<link href="https://fonts.googleapis.com/css2?family=Domine:wght@700&family=Montserrat:ital,wght@0,400;0,800;1,700;1,800&display=swap" rel="stylesheet">
<style>
  :root {
    --charcoal: #414646;
    --brand-blue: #1a95c8;
    --ink: #111111;
    --paper: #ffffff;
  }
  html, body { margin: 0; padding: 0; overflow: hidden; background: var(--paper); }
  .page {
    position: relative;
    width: 848px;
    height: 1200px;
    overflow: hidden;
    background: var(--paper);
    font-family: "Montserrat", sans-serif;
    color: var(--ink);
  }
  .title-band {
    position: absolute;
    left: 0; top: 65px;
    width: 848px; height: 126px;
    background: var(--charcoal);
    box-shadow: 0 2px 3px rgba(0,0,0,0.25);
  }
  .doc-title {
    position: absolute;
    left: 87px; top: 86px;
    margin: 0;
    font-weight: 800;
    font-size: 41px;
    line-height: 45px;
    letter-spacing: 0.3px;
    color: var(--paper);
  }
  .side-bar {
    position: absolute;
    left: 674px; top: 0;
    width: 71px; height: 1200px;
    background: var(--brand-blue);
  }
  .page-number {
    position: absolute;
    left: 674px; width: 71px;
    top: 1124px;
    text-align: center;
    font-weight: 800;
    font-size: 24px;
    color: var(--paper);
  }
  .content {
    position: absolute;
    left: 81px; top: 208px;
    width: 585px;
  }
  .section-title {
    margin: 0 0 20px;
    font-weight: 800;
    font-style: italic;
    font-size: 27px;
    line-height: 34px;
    color: var(--brand-blue);
  }
  .article-title {
    margin: 0 0 21px;
    font-family: "Domine", serif;
    font-weight: 700;
    font-size: 17px;
    line-height: 22px;
  }
  .pillar {
    margin: 0 0 21px;
    font-weight: 700;
    font-style: italic;
    font-size: 17px;
    line-height: 22px;
    text-decoration: underline;
    text-underline-offset: 2px;
  }
  .body-text {
    margin: 0 0 21px;
    font-size: 17px;
    line-height: 21.5px;
  }
</style>
</head>
<body>
<div class="page">
  <div class="title-band"></div>
  <h1 class="doc-title">BRENWICK CHAMBER<br>BYLAWS</h1>
  <div class="side-bar"></div>
  <div class="page-number">1</div>

  <main class="content">
    <h2 class="section-title">1.0 General</h2>

    <h3 class="article-title">1.1: Name</h3>
    <p class="body-text">This organization is incorporated under the laws of the State of Oregon and shall be known as the Brenwick Area Chamber of Commerce (“Chamber").</p>

    <h3 class="article-title">1.2: Purpose</h3>
    <p class="body-text">The Brenwick Area Chamber of Commerce is organized to build a strong community where businesses can thrive by fostering:</p>

    <h4 class="pillar">Positive Connections</h4>
    <p class="body-text">Meaningful connections that help our business community thrive, and connect our members with customers, partners, mentors and friends.</p>

    <h4 class="pillar">Business Growth</h4>
    <p class="body-text">The growth of local businesses through effective promotion and business development opportunities.</p>

    <h4 class="pillar">Community Engagement</h4>
    <p class="body-text">Community engagement through programs and events, we can influence the culture of our community and enhance the quality of life.</p>

    <h4 class="pillar">Collaborative&nbsp; Advocacy</h4>
    <p class="body-text">Advocacy for a healthy economy and aligning businesses and government, we provide a voice for initiatives relevant to our members.</p>

    <h3 class="article-title">1.3: Service Area</h3>
    <p class="body-text">The service area of the Chamber includes the region of Brenwick, which includes, Harlow Point, Seabrook, Cove City, and Marrowby. The service area may also include Brenwick County and areas beyond.</p>
  </main>
</div>
</body>
</html>
```